New Sticker Design Project

Hello, Thank you for the great design of the tape. I would like to hire you to create another design to match the tape for the side of the box. 4" X 6"
Text: Perishable, Living Food as Medicine, Please Keep Cold, Do Not Delay, Quick Delivery Necessary, Place in Refrigerator Immediately upon Delivery
With symbols for Cold, and time-sensitive. Could use all caps if the design looks good. Same text font and color scheme to match the look of the tape. Logo if space. This needs to stand out on the shipping box which is brown boxes. Thanks again. !
Target Market(s)
Shipping box informational Sticker Outside
Requirements
Must have
- Similar matching look to the tape. The word PERISHABLE needs to be dominate!
Nice to have
- bold easy to read eye catching information for Quorvel and customer
Should not have
- Clutter

```html
<!DOCTYPE html>
<html lang="en">
<head>
<meta charset="utf-8">
<title>Green Tide Algae – Shipping Sticker</title>
<link href="https://fonts.googleapis.com/css2?family=Oswald:wght@600;700&family=Barlow+Condensed:ital,wght@1,600&family=Montserrat:wght@500&display=swap" rel="stylesheet">
<style>
  :root{
    --ink:#3a3a3a;
    --paper:#ffffff;
    --bg:#ffffff;
    --brand-green:#2f8a7a;
  }
  html,body{margin:0;padding:0;overflow:hidden;}
  body{width:793px;height:1200px;background:var(--bg);position:relative;}
  .sticker{position:absolute;left:30px;top:355px;width:733px;height:489px;background:var(--paper);}
  .frame-bar{position:absolute;background:var(--ink);}
  .brand-mark{position:absolute;left:50%;top:66px;width:44px;height:44px;margin-left:-22px;border-radius:50%;background:var(--brand-green);}
  .brand-name{position:absolute;left:0;right:0;text-align:center;font-family:"Oswald",sans-serif;font-weight:700;color:var(--ink);font-size:42px;line-height:1;letter-spacing:1px;margin:0;}
  .brand-name.line-1{top:120px;}
  .brand-name.line-2{top:170px;}
  .tagline{position:absolute;left:50%;top:221px;transform:translateX(-50%);border:1.5px solid var(--ink);padding:1px 18px;font-family:"Montserrat",sans-serif;font-weight:500;font-size:10px;letter-spacing:.5px;color:var(--ink);white-space:nowrap;line-height:12px;}
  .notice{position:absolute;display:flex;align-items:center;}
  .notice svg{width:44px;height:44px;flex:none;stroke:var(--ink);fill:none;stroke-width:2.2;stroke-linecap:round;stroke-linejoin:round;}
  .notice-label{position:absolute;font-family:"Barlow Condensed",sans-serif;font-style:italic;font-weight:600;font-size:17px;line-height:22px;color:var(--ink);text-transform:uppercase;white-space:nowrap;}
</style>
</head>
<body>
<section class="sticker">
  <div class="frame-bar" style="left:0;top:0;width:355px;height:24px"></div>
  <div class="frame-bar" style="left:380px;top:0;width:353px;height:24px"></div>
  <div class="frame-bar" style="left:0;top:0;width:24px;height:232px"></div>
  <div class="frame-bar" style="left:0;top:258px;width:24px;height:231px"></div>
  <div class="frame-bar" style="right:0;top:0;width:24px;height:232px"></div>
  <div class="frame-bar" style="right:0;top:258px;width:24px;height:231px"></div>
  <div class="frame-bar" style="left:0;bottom:0;width:355px;height:24px"></div>
  <div class="frame-bar" style="left:380px;bottom:0;width:353px;height:24px"></div>

  <div class="brand-mark"></div>
  <h1 class="brand-name line-1">GREEN TIDE</h1>
  <h1 class="brand-name line-2">ALGAE</h1>
  <div class="tagline">A SIP OF VITALITY</div>

  <div class="notice" style="left:46px;top:286px">
    <svg viewBox="0 0 44 44"><rect x="4" y="3" width="36" height="38"/><path d="M10 14c4-4 10-4 14 0-4 4-10 4-14 0zM24 14l6-4v8z"/><circle cx="18" cy="28" r="3"/><circle cx="24" cy="28" r="3"/><circle cx="21" cy="33" r="3"/></svg>
  </div>
  <span class="notice-label" style="left:104px;top:297px">Perishable</span>

  <div class="notice" style="left:238px;top:286px">
    <svg viewBox="0 0 44 44"><path d="M4 12h14M11 5v14M6 7l10 10M16 7L6 17"/><path d="M26 6a4 4 0 0 1 8 0v20a7 7 0 1 1-8 0z"/><circle cx="30" cy="31" r="3"/><path d="M30 28V16"/></svg>
  </div>
  <span class="notice-label" style="left:305px;top:286px">Please<br>Keep Cold</span>

  <div class="notice" style="left:420px;top:286px">
    <svg viewBox="0 0 44 44"><path d="M12 8h18v24H12M30 16h6l6 7v9h-12"/><circle cx="16" cy="34" r="4"/><circle cx="34" cy="34" r="4"/><path d="M2 14h8M4 20h8M2 26h8"/></svg>
  </div>
  <span class="notice-label" style="left:498px;top:286px">Quick Delivery<br>Necessary</span>

  <div class="notice" style="left:46px;top:380px">
    <svg viewBox="0 0 44 44"><path d="M8 24h28a14 12 0 0 1-28 0zM4 40h36"/><path d="M22 22v-8M22 16c-6 0-8-6-8-8 6 0 8 4 8 8zM22 16c6 0 8-6 8-8-6 0-8 4-8 8z"/></svg>
  </div>
  <span class="notice-label" style="left:104px;top:380px">Living Food<br>As Medicine</span>

  <div class="notice" style="left:238px;top:380px">
    <svg viewBox="0 0 44 44"><path d="M26 39A18 18 0 1 1 39 24"/><path d="M22 11v11h-8"/><circle cx="33" cy="34" r="8"/><path d="M29 34l3 3 5-6"/></svg>
  </div>
  <span class="notice-label" style="left:305px;top:380px">Do Not<br>Delay</span>

  <div class="notice" style="left:420px;top:380px">
    <svg viewBox="0 0 44 44"><rect x="11" y="3" width="22" height="38" rx="2"/><path d="M11 16h22M15 8v4M15 21v6"/></svg>
  </div>
  <span class="notice-label" style="left:498px;top:380px">Place in Refrigerator<br>Immediately upon Delivery</span>
</section>
</body>
</html>
```